Men’s hair skin and beard line

I own a men’s salon in Texas and are beginning to expand its market into the men’s retail line and already have it being manufactured out of the UK. It’s paraben free, vegan, sulphate free. I need a better brand look for the packaging. This script font is a bit hard to read. I want it masculine yet clean lines. All colors even gold or silver are welcomed. Bottle choices are silver canisters, white or black.

Target Market(s)

Men

Industry/Entity Type

Men’s hair skin and beard industry. Retail centers, high end barbers, and gyms

Font styles to use
Other font styles liked:
• Montserrat ,helvetica neue, or lato font

Colors
0054AA
0677BA
7BADD7
CADEEF
E8F1F8
0094D4
00A9DD
6FCCEA
C7EBF8
E9F6FB
00AB8E
00BBA5
67D7C9
C6EFE9
E9F9F6

Requirements
Must have
• Logo and name
Nice to have
• I’m open to all.
Should not have
• Not feminine

```html
<!DOCTYPE html>
<html lang="en">
<head>
<meta charset="utf-8">
<title>Vantage Heritage Line – Sharing Gel Label</title>
<link rel="stylesheet" href="https://fonts.googleapis.com/css2?family=Montserrat:wght@700&family=Lato:wght@300;400&display=swap">
<style>
  :root {
    --canvas: #ffffff;
    --label-black: #0b0b0b;
    --label-deep: #151515;
    --facet-grey: #5a5a5a;
    --gold: #8f7d3c;
    --ink-light: #d9d9d9;
    --ink-muted: #bdbdbd;
  }
  html, body {
    margin: 0;
    width: 1200px;
    height: 983px;
    overflow: hidden;
    background: var(--canvas);
  }
  .canvas {
    position: relative;
    width: 1200px;
    height: 983px;
  }
  .label {
    position: absolute;
    left: 410px;
    top: 26px;
    width: 380px;
    height: 930px;
    background: var(--label-black);
    overflow: hidden;
    font-family: "Lato", sans-serif;
  }
  .facet-texture {
    position: absolute;
    inset: 0;
    background:
      radial-gradient(ellipse 70% 55% at 100% 95%, rgba(150,150,150,0.75), rgba(90,90,90,0.35) 45%, rgba(0,0,0,0) 75%),
      linear-gradient(200deg, rgba(0,0,0,0) 35%, rgba(70,70,70,0.45) 100%);
  }
  .brand-name {
    position: absolute;
    left: 30px;
    top: 78px;
    height: 495px;
    writing-mode: vertical-rl;
    transform: rotate(180deg);
    font-family: "Montserrat", sans-serif;
    font-weight: 700;
    font-size: 78px;
    line-height: 1;
    letter-spacing: 6px;
    color: var(--gold);
    text-align: center;
  }
  .line-name {
    position: absolute;
    left: 122px;
    top: 78px;
    height: 495px;
    writing-mode: vertical-rl;
    transform: rotate(180deg);
    font-family: "Lato", sans-serif;
    font-weight: 300;
    font-size: 34px;
    line-height: 1;
    letter-spacing: 15px;
    color: var(--ink-light);
    text-align: center;
    white-space: nowrap;
  }
  .brand-tag {
    position: absolute;
    right: 30px;
    top: 96px;
    display: flex;
    align-items: center;
    gap: 7px;
    font-family: "Lato", sans-serif;
    font-weight: 400;
    font-size: 15px;
    letter-spacing: 2px;
    color: var(--gold);
  }
  .brand-tag .mark-square {
    width: 12px;
    height: 12px;
    background: var(--gold);
  }
  .product-name {
    position: absolute;
    left: 28px;
    top: 602px;
    margin: 0;
    font-weight: 300;
    font-size: 45px;
    line-height: 44px;
    letter-spacing: 1px;
    color: var(--gold);
  }
  .product-type {
    position: absolute;
    left: 34px;
    top: 702px;
    font-size: 11px;
    letter-spacing: 3.2px;
    color: var(--ink-muted);
  }
  .usage-note {
    position: absolute;
    left: 34px;
    top: 740px;
    width: 230px;
    margin: 0;
    font-size: 11.5px;
    line-height: 14px;
    color: var(--ink-light);
  }
  .volume {
    position: absolute;
    left: 120px;
    top: 845px;
    font-size: 20px;
    color: var(--ink-light);
  }
</style>
</head>
<body>
<main class="canvas">
  <section class="label">
    <div class="facet-texture" role="img" aria-label="Dark low-poly faceted texture fading to grey toward the lower right"></div>
    <div class="brand-name">VANTAGE</div>
    <div class="line-name">HERITAGE LINE</div>
    <div class="brand-tag"><span class="mark-square"></span>VANTAGE</div>
    <h1 class="product-name">SHARING<br>GEL</h1>
    <div class="product-type">Pre Shave Softening Gel</div>
    <p class="usage-note">When gel is applied<br>by massaging,it will rapidly soften<br>the beard, ensuring the shaving blade<br>can easily glide and thus prevent<br>irritation of the skin</p>
    <div class="volume">250ml / 8.4fl.oz</div>
  </section>
</main>
</body>
</html>
```